Business Cards,Stationary, HTML e-mail template
New Employee Benefits Business
Business Cards,Stationary, HTML e-mail template -
Creative Brief
Professional
Peter L. Marsh GBDS
Chief Benefits Guru
Suite 410 27 Kestrel Lane Webster, NY 14580
PMarsh@HarborlineWorkforce.com
www.HarborlineWorkforce.com
"Paperless" Open Enrollment Customize a 3-year Benefits Vision Survive a DOL Investigation Implement HR Services Portal

```html
<!DOCTYPE html>
<html lang="en">
<head>
<meta charset="utf-8">
<title>Harborline Workforce — Stationery Set</title>
<link href="https://fonts.googleapis.com/css2?family=Cinzel:wght@600&family=Open+Sans:wght@400;600&display=swap" rel="stylesheet">
<style>
  :root {
    --stage: #2e2f31;
    --paper: #ffffff;
    --paper-shade: #eef0f3;
    --blue-deep: #0b2a9c;
    --blue-mid: #1f4fd1;
    --blue-light: #5f9af2;
    --ink: #3a3f47;
    --ink-soft: #8a9099;
  }
  * { box-sizing: border-box; margin: 0; padding: 0; }
  html, body { width: 1200px; height: 643px; overflow: hidden; }
  body {
    background: var(--stage);
    position: relative;
    font-family: "Open Sans", Arial, sans-serif;
    color: var(--ink);
  }
  .piece { position: absolute; background: var(--paper); overflow: hidden; }

  /* brand lockup */
  .brand { display: flex; align-items: center; gap: 5px; }
  .brand-dot { border-radius: 50%; background: var(--blue-mid); flex: none; }
  .brand-name { font-family: "Cinzel", Georgia, serif; font-weight: 600; color: var(--blue-deep); letter-spacing: .5px; }

  .contact-name { font-family: "Cinzel", Georgia, serif; font-weight: 600; color: var(--ink); font-size: 9px; letter-spacing: .4px; }
  .contact-title { font-size: 6px; color: var(--ink-soft); margin-bottom: 5px; }
  .contact-line { font-size: 5.5px; line-height: 8px; color: var(--ink-soft); }

  /* business card front */
  .card-front {
    left: 84px; top: 77px; width: 199px; height: 115px;
    background: radial-gradient(circle at 30% 45%, var(--blue-light), var(--blue-mid) 45%, var(--blue-deep));
    border-radius: 3px;
  }
  .card-front .brand { position: absolute; left: 22px; top: 42px; }
  .card-front .brand-dot { width: 28px; height: 28px; background: #ffffff; opacity: .9; }
  .card-front .tagline { position: absolute; left: 60px; top: 52px; font-size: 6px; color: #dfe9ff; }

  /* business card back */
  .card-back { left: 84px; width: 199px; height: 110px; border-radius: 3px; background: linear-gradient(180deg, var(--paper), var(--paper-shade)); }
  .card-back::before { content: ""; position: absolute; left: 0; top: 22px; width: 4px; height: 34px; background: var(--blue-mid); }
  .card-back .brand { position: absolute; right: 12px; top: 14px; }
  .card-back .brand-dot { width: 10px; height: 10px; }
  .card-back .brand-name { font-size: 11px; }
  .card-back .details { position: absolute; left: 14px; top: 40px; }

  /* letterhead */
  .letterhead { left: 300px; top: 84px; width: 403px; height: 511px; }
  .letterhead .brand { position: absolute; left: 50%; top: 40px; transform: translateX(-50%); }
  .letterhead .brand-dot { width: 14px; height: 14px; }
  .letterhead .brand-name { font-size: 16px; }
  .letterhead .footer-band { position: absolute; left: 0; bottom: 22px; width: 4px; height: 20px; background: var(--blue-mid); }
  .letterhead .footer { position: absolute; left: 14px; bottom: 22px; }

  /* wide card */
  .wide-card { left: 713px; top: 144px; width: 408px; height: 72px; }
  .wide-card .band {
    position: absolute; left: 0; top: 0; width: 100%; height: 100%;
    background: linear-gradient(90deg, var(--blue-deep), var(--blue-mid) 25%, var(--paper) 26%);
  }
  .wide-card .details { position: absolute; left: 150px; top: 10px; }
  .wide-card .contact-line { font-size: 5px; line-height: 7px; }

  /* envelope front */
  .envelope { left: 713px; top: 228px; width: 408px; height: 168px; }
  .envelope .brand { position: absolute; right: 22px; top: 18px; }
  .envelope .brand-dot { width: 14px; height: 14px; }
  .envelope .brand-name { font-size: 16px; }
  .envelope .accent { position: absolute; left: 0; top: 64px; width: 4px; height: 22px; background: var(--blue-mid); }
  .envelope .return { position: absolute; left: 14px; top: 64px; }

  /* envelope back */
  .envelope-back { left: 713px; top: 413px; width: 408px; height: 182px; background: linear-gradient(180deg, var(--paper-shade), var(--paper)); }
  .envelope-back svg { position: absolute; left: 0; top: 0; }
  .envelope-back .seal { position: absolute; left: 197px; top: 32px; width: 14px; height: 14px; border-radius: 50%; background: #ffffff; opacity: .9; }
</style>
</head>
<body>

<section class="piece card-front" aria-label="Business card front">
  <div class="brand"><span class="brand-dot"></span></div>
  <p class="tagline">Employee benefits, made simple.</p>
</section>

<section class="piece card-back" style="top:216px" aria-label="Business card">
  <div class="brand"><span class="brand-dot"></span><span class="brand-name">HARBORLINE</span></div>
  <div class="details">
    <p class="contact-name">PETER L. MARSH GBDS</p>
    <p class="contact-title">Chief Benefits Guru</p>
    <p class="contact-line">Suite 410 27 Kestrel Lane Webster, NY 14580</p>
    <p class="contact-line">Office 585.555.0142</p>
    <p class="contact-line">PMarsh@HarborlineWorkforce.com</p>
    <p class="contact-line">www.HarborlineWorkforce.com</p>
  </div>
</section>

<section class="piece card-back" style="top:353px" aria-label="Business card">
  <div class="brand"><span class="brand-dot"></span><span class="brand-name">HARBORLINE</span></div>
  <div class="details">
    <p class="contact-name">PETER L. MARSH GBDS</p>
    <p class="contact-title">Chief Benefits Guru</p>
    <p class="contact-line">Suite 410 27 Kestrel Lane Webster, NY 14580</p>
    <p class="contact-line">Office 585.555.0142</p>
    <p class="contact-line">PMarsh@HarborlineWorkforce.com</p>
    <p class="contact-line">www.HarborlineWorkforce.com</p>
  </div>
</section>

<section class="piece card-back" style="top:487px" aria-label="Business card">
  <div class="brand"><span class="brand-dot"></span><span class="brand-name">HARBORLINE</span></div>
  <div class="details">
    <p class="contact-name">PETER L. MARSH GBDS</p>
    <p class="contact-title">Chief Benefits Guru</p>
    <p class="contact-line">Suite 410 27 Kestrel Lane Webster, NY 14580</p>
    <p class="contact-line">Office 585.555.0142</p>
    <p class="contact-line">PMarsh@HarborlineWorkforce.com</p>
    <p class="contact-line">www.HarborlineWorkforce.com</p>
  </div>
</section>

<section class="piece letterhead" aria-label="Letterhead">
  <div class="brand"><span class="brand-dot"></span><span class="brand-name">HARBORLINE</span></div>
  <span class="footer-band"></span>
  <div class="footer">
    <p class="contact-line">Suite 410 27 Kestrel Lane Webster, NY 14580</p>
    <p class="contact-line">Office 585.555.0142 · www.HarborlineWorkforce.com</p>
  </div>
</section>

<section class="piece wide-card" aria-label="Compliment card">
  <div class="band"></div>
  <div class="details">
    <p class="contact-name">PETER L. MARSH GBDS</p>
    <p class="contact-title">Chief Benefits Guru</p>
    <p class="contact-line">Suite 410 27 Kestrel Lane Webster, NY 14580</p>
    <p class="contact-line">Office 585.555.0142</p>
    <p class="contact-line">PMarsh@HarborlineWorkforce.com · www.HarborlineWorkforce.com</p>
  </div>
</section>

<section class="piece envelope" aria-label="Envelope front">
  <div class="brand"><span class="brand-dot"></span><span class="brand-name">HARBORLINE</span></div>
  <span class="accent"></span>
  <div class="return">
    <p class="contact-line">Suite 410 27 Kestrel Lane</p>
    <p class="contact-line">Webster, NY 14580</p>
    <p class="contact-line">www.HarborlineWorkforce.com</p>
  </div>
</section>

<section class="piece envelope-back" aria-label="Envelope back">
  <svg width="408" height="182" viewBox="0 0 408 182">
    <defs>
      <linearGradient id="flap" x1="0" y1="0" x2="0" y2="1">
        <stop offset="0" stop-color="#1f4fd1"/>
        <stop offset="1" stop-color="#0b2a9c"/>
      </linearGradient>
    </defs>
    <path d="M0 0 H408 V22 Q300 30 230 60 Q204 72 178 60 Q108 30 0 22 Z" fill="url(#flap)"/>
  </svg>
  <span class="seal"></span>
</section>

</body>
</html>
```